Business Cards for Volmar Pike, a law firm

We changed our firm's name from "Volmar & Pike LLP" to "Volmar Pike", we need to update our cards with a new design. We like the overall look of the back but the front side of the cards (see attached mockup) needs a refreshed look. I also attach our current logo so you can get rid of that LLP and &. We have a new address as well (not same as on mockup).

Target Market(s)

Clients of law firm

Industry/Entity Type

Law Firm

Contact Information for Business Card

Frontsides:

Lorenzo T. Volmar
Partner
Tel: (555) 710-2284 ext. 101
Fax: (555) 382-6419
Email: lvolmar@vplegal.example

Simon K. Pike
Partner
Tel: (555) 710-2284 ext. 102
Fax: (555) 382-6419
Email: simonpike@vplegal.example

Omar J. Benedek
Barrister
Tel: (555) 710-2284 ext. 104
Fax: (555) 382-6419
Email: obenedek@vplegal.example

The back side should be crimson red (see mockup) with the logo (please update it to remove the & and the LLP, you can modify it a bit to make it tasteful if need be). Our new address is

71 Marrowby Rd W, Suite 208
Toronto, ON M9X 3K5

After our address, please also include our website www.vplegal.example

Font styles to use
Sans Serif

Colors
ec2027
ffffff
000000

Requirements
Must have
• PLEASE NOTE: our firm's colour is more of a darker/crimson red, not a vibrant red.
• The front should have space for the lawyer's name, title, phone number (with extension), fax number, and email.
• If you're going to add those yourself, the info for the frontside is in the "Business Card Details" section (three lawyers that need their own cards).
Nice to have
• We like the backside of our current cards, just update it with our new address (one address now instead of 2), and a slightly modified logo (not a new logo altogether).
• The frontside should be refreshed with a better look (think minimalist, professional and modern), although still predominantly white-based background.
Should not have
• No scales of justice or other cheesy lawyer stereotype symbols! :-)

```html
<!DOCTYPE html>
<html lang="en">
<head>
<meta charset="utf-8">
<title>Volmar Pike — Business Cards</title>
<link rel="stylesheet" href="https://fonts.googleapis.com/css2?family=Arimo:wght@400;700&display=swap">
<style>
  :root {
    --crimson: #a8101a;
    --crimson-deep: #5e0409;
    --crimson-dark: #2a0204;
    --ink: #111111;
    --paper: #ffffff;
    --paper-shade: #cfcfcf;
    --stage: #e9e9e9;
    --muted-white: #f2e6e6;
  }
  * { box-sizing: border-box; margin: 0; padding: 0; }
  html, body {
    width: 1200px;
    height: 941px;
    overflow: hidden;
  }
  body {
    background: var(--stage);
    font-family: "Arimo", Arial, sans-serif;
    display: flex;
    align-items: center;
    justify-content: center;
    gap: 60px;
  }
  .card {
    position: relative;
    width: 520px;
    height: 298px;
    border-radius: 3px;
    box-shadow: 0 6px 18px rgba(0,0,0,0.18);
    overflow: hidden;
  }

  /* Front side */
  .card--front {
    background: radial-gradient(ellipse at 100% 0%, #5a5a5a 0%, var(--paper-shade) 28%, #f4f4f4 60%, var(--paper) 100%);
    color: var(--ink);
  }
  .card--front .brand {
    position: absolute;
    left: 34px;
    top: 40px;
    display: flex;
    align-items: center;
    gap: 12px;
  }
  .brand__dot {
    width: 30px;
    height: 30px;
    border-radius: 50%;
    background: var(--crimson);
  }
  .brand__name {
    font-weight: 700;
    font-size: 26px;
    letter-spacing: 0.5px;
  }
  .card--front .brand__name { color: var(--ink); }

  .card--front .divider {
    position: absolute;
    left: 34px;
    right: 34px;
    top: 150px;
    height: 2px;
    background: linear-gradient(90deg, var(--crimson) 0%, var(--crimson-deep) 45%, var(--ink) 100%);
  }
  .person {
    position: absolute;
    right: 34px;
    top: 88px;
    text-align: right;
  }
  .person__name {
    font-weight: 700;
    font-size: 22px;
  }
  .person__title {
    font-size: 15px;
    margin-top: 4px;
  }
  .contact {
    position: absolute;
    right: 34px;
    top: 172px;
    text-align: right;
    font-size: 14px;
    line-height: 1.55;
  }

  /* Back side */
  .card--back {
    background: radial-gradient(ellipse at 30% 20%, var(--crimson) 0%, var(--crimson-deep) 60%, var(--crimson-dark) 100%);
    color: var(--paper);
  }
  .card--back .brand {
    position: absolute;
    right: 40px;
    top: 70px;
    display: flex;
    align-items: center;
    gap: 12px;
  }
  .card--back .brand__dot { background: var(--paper); }
  .card--back .brand__name { color: var(--paper); }
  .card--back .divider {
    position: absolute;
    left: 40px;
    right: 40px;
    top: 150px;
    height: 2px;
    background: linear-gradient(90deg, rgba(0,0,0,0.9) 0%, var(--paper) 55%, rgba(255,255,255,0.2) 100%);
  }
  .address {
    position: absolute;
    left: 40px;
    top: 176px;
    font-size: 14px;
    line-height: 1.7;
    color: var(--muted-white);
  }
</style>
</head>
<body>
  <section class="card card--front" aria-label="Business card front">
    <div class="brand">
      <span class="brand__dot"></span>
      <span class="brand__name">Volmar Pike</span>
    </div>
    <div class="person">
      <p class="person__name">Lorenzo T. Volmar</p>
      <p class="person__title">Partner</p>
    </div>
    <div class="divider"></div>
    <div class="contact">
      <p>Tel: (555) 710-2284 ext. 101</p>
      <p>Fax: (555) 382-6419</p>
      <p>Email: lvolmar@vplegal.example</p>
    </div>
  </section>

  <section class="card card--back" aria-label="Business card back">
    <div class="brand">
      <span class="brand__dot"></span>
      <span class="brand__name">Volmar Pike</span>
    </div>
    <div class="divider"></div>
    <div class="address">
      <p>71 Marrowby Rd W, Suite 208 Toronto, ON M9X 3K5</p>
      <p>www.vplegal.example</p>
    </div>
  </section>
</body>
</html>
```